Online Psychiatry business - Business Card

I need a business card design. The target audience is busy professionals of any field (this therapy appeals best to 24-35 year olds). It involves psychiatry by tele-medicine (or video-conference). Nothing on it should be a giveaway that it's about mental health. Professional design with silver or gold as the primary colors appeals to me. The card must be as simple and as uncluttered as possible. Some color and flowing design on the edge of the card appeals to me.
CrestMindLink.com should probably appear in the center of the card and stand out, i.e. bold lettering, and easy to read, no cursive, but Ariel Black. Some where below this, should appear "Too Busy to Take Care of Yourself? Think again." Since this isn't office based, I don't think an office address is necessary and limits clutter.
Information that does need to appear is my name: Gerald Whitcombe, MD
General phone number: 541-876-2209. I'm hoping to get an 24-hour answering service soon so leave a little room for this. In addition I want to include two email addresses:
CrestMindLink@maildrop-box.com and CrestMind247@maildrop-box.com
Updates

I like the designs. I would like someone to put the website in bold in the center

 as most have been doing with a smaller font reminder nearby saying "No time" etc.
but I'd like to put my name down in the corner with the rest of the contact material.
Black print against a white or grey background appeals to me, with darker silver artwork near the sides (simple abstract, like wavy lines or something you can one up with that works. 
thanks

I ve tried to provide as much feedback as possible given my time limits, so if you have extra questions, please feel free to email. I tried to attach a file of a business card I really like but make be difficult to actually manufacture. I'm going to send you a link to the photo. The card has a pull tab. There is not much information on the outside. In fact, if you were to design the outside, I would just print : Too Busy to Take Care of Yourself? Think Again.

When you pull the tab the remaining information is on the bottom half of the card. Please don't use the color pink!!!!
http://www.layoutgallerypost.com/2009/05/100-clever-card-ideas/
It is the 39th photo on the list, about 2/3ds of the way down the page. It is titled: Faltenkästli

#7 and #16 have an appeal to me, except for the dot patterns
Hope this helps

I'm running out of time and energy. I 've been trying to give do down the list and give  individual feedback but I won't be able to do that anymore.

So if you have any specific questions, write me, and again thank you for all your effort!!

I know i received your files, including your zip files, Plonix,

but Gideon, did you send me the files including ZIP on project 5914386?
thanks

Target Market(s)

Working professionals and executive, attorneys, etc.

Industry/Entity Type

Business

Logo Text

Don't Have Time to Take Care of Yourself? Think Again.

Logo styles of interest
Pictorial/Combination Logo
Wordmark Logo
Other font styles liked:
• Ariel Black appeals to me the most

Requirements
Must have
• Want to emphasize that the website must be obvious, easily found (The CrestMindLink.com)
For that reason i'd like the card to be white, and minimal decoration on one or both sides just to add some style and color
Nice to have
• A Very uncluttered, elegant design, and something that makes it stick in your head-doesn't everyone want the last?
Should not have
• Nothing on the card that give it away that this is about psychiatry, such as brain or other symbol, but also nothing that gives it away as a medical business, such as a stethoscope or red cross or anything.

```html
<!DOCTYPE html>
<html lang="en">
<head>
<meta charset="utf-8">
<title>CrestMindLink Business Card</title>
<link href="https://fonts.googleapis.com/css2?family=Montserrat:wght@400;800;900&display=swap" rel="stylesheet">
<style>
  :root {
    --backdrop: #e9e8e4;
    --card: #f7f7f5;
    --ink: #111111;
    --silver: #7a7a7a;
    --ink-soft: #2a2a2a;
  }
  * { margin: 0; padding: 0; box-sizing: border-box; }
  html, body {
    width: 1200px; height: 960px; overflow: hidden;
    background: var(--backdrop);
    font-family: "Montserrat", Arial, sans-serif;
  }
  .card-set {
    position: absolute; top: 0; left: 0; width: 1200px; height: 960px;
    display: flex; align-items: center; justify-content: center; gap: 40px;
  }
  .card {
    position: relative;
    width: 540px; height: 309px;
    background: var(--card);
    box-shadow: 0 2px 6px rgba(0,0,0,0.12);
  }
  /* Front side */
  .card-front .reminder {
    position: absolute; right: 30px; top: 112px;
    font-size: 13px; font-weight: 400; color: var(--ink-soft);
  }
  .card-front .tagline {
    position: absolute; left: 56px; top: 178px;
    font-size: 25px; font-weight: 900; letter-spacing: -0.3px;
    background: linear-gradient(90deg, var(--ink) 35%, var(--silver) 100%);
    -webkit-background-clip: text; background-clip: text; color: transparent;
  }
  /* Back side */
  .card-back .website {
    position: absolute; left: 26px; top: 86px;
    font-size: 41px; font-weight: 900; letter-spacing: -1px;
    color: var(--ink);
  }
  .card-back .contact {
    position: absolute; left: 30px; top: 178px;
    color: var(--ink-soft); font-size: 14px; line-height: 1.35;
  }
  .card-back .contact .name {
    font-weight: 800; font-size: 13px; margin-bottom: 4px; color: var(--ink);
  }
</style>
</head>
<body>
  <main class="card-set">
    <section class="card card-front" aria-label="Card front">
      <p class="reminder">Think again...</p>
      <h1 class="tagline">Too Busy to Take Care of Yourself?</h1>
    </section>
    <section class="card card-back" aria-label="Card back">
      <h2 class="website">CrestMindLink.com</h2>
      <div class="contact">
        <p class="name">Gerald Whitcombe, MD</p>
        <p class="phone">541-876-2209</p>
        <p class="email">CrestMindLink@maildrop-box.com</p>
        <p class="email">CrestMind247@maildrop-box.com</p>
      </div>
    </section>
  </main>
</body>
</html>
```